Emergency Medical Training and Events Company Business Needs Business Card Design

We are in need of a business card for our dynamic company expanding its customer base and need to be easily contacted and identified for when we visit with government officials, potential EMS / Fire agencies and county coordinators to arrange for training programs for first responders to better prepare them for critical thinking at critical incidents.

Target Market(s)

EMS/Fire and Event Promoters

Industry/Entity Type

Medical

Contact Information for Business Card

Two cards, comparable designs:

Martin K. Halvey, Principal, m.halvey@rvqtlo.com
Owen Tash, Event and Training Specialist, o.tash@rvqtlo.com

Font styles to use
Other font styles liked:
• Cambria

Colors

Designer to choose colors to be used in the design.

Requirements
Must have
• Company Logo, Spots for Name, Title, Phone Number, Email, Website
• A bullet list stating that we offer, QRB CPR and First Aid Instructors, Hold the Line Instructors, Event EMS, CME's, MCI Training and Planning. We prefer to have a black background for the card but if you can make a blue or white card stand out we would review that as well.
Should not have
• Tacky logos or special sayings ... simple, elegant, professional is the look we seek

```html
<!DOCTYPE html>
<html lang="en">
<head>
<meta charset="utf-8">
<title>R.Q.T. Solutions of ON – Business Card</title>
<link rel="stylesheet" href="https://fonts.googleapis.com/css2?family=Caladea:wght@400;700&display=swap">
<style>
  :root {
    --navy: #0d1b52;
    --red: #d0202a;
    --white: #ffffff;
    --backdrop: #e8e4dd;
    --ink: #0d1b52;
  }
  * { margin: 0; padding: 0; box-sizing: border-box; }
  html, body { width: 900px; height: 1200px; overflow: hidden; }
  body {
    background: var(--backdrop);
    position: relative;
    font-family: "Caladea", Cambria, Georgia, serif;
  }
  .card {
    position: absolute;
    left: 82px;
    width: 733px;
    height: 429px;
    border-radius: 22px;
    overflow: hidden;
    background: var(--navy);
    box-shadow: 0 6px 14px rgba(0,0,0,0.25);
  }
  .card--front { top: 137px; }
  .card--back { top: 632px; }
  .card__shape { position: absolute; inset: 0; }

  .brand-mark {
    position: absolute;
    left: 91px; top: 135px;
    width: 140px;
    text-align: center;
    color: var(--white);
    font-weight: 700;
  }
  .brand-mark__dot {
    width: 70px; height: 70px;
    margin: 0 auto 14px;
    border-radius: 50%;
    background: var(--white);
  }
  .brand-mark__name { font-size: 26px; letter-spacing: 1px; }

  .company {
    position: absolute;
    left: 389px; top: 50px;
    font-size: 27px;
    line-height: 36px;
    font-weight: 700;
    color: var(--ink);
  }
  .company__accent { color: var(--red); }

  .person { position: absolute; left: 389px; top: 178px; }
  .person__name { font-size: 21px; font-weight: 700; color: var(--ink); line-height: 28px; }
  .person__title { font-size: 16px; color: var(--red); line-height: 22px; }

  .contact-list {
    position: absolute;
    left: 389px; top: 248px;
    list-style: none;
  }
  .contact-list__item {
    display: flex;
    align-items: center;
    height: 34.5px;
    font-size: 18px;
    color: var(--ink);
  }
  .contact-list__icon {
    width: 23px; height: 23px;
    margin-right: 13px;
    flex: none;
  }

  .lockup {
    position: absolute;
    left: 175px; top: 168px;
    display: flex;
    align-items: center;
    color: var(--white);
    font-weight: 700;
  }
  .lockup__dot {
    width: 80px; height: 80px;
    border-radius: 50%;
    background: var(--white);
    margin-right: 22px;
  }
  .lockup__name { line-height: 1; }
  .lockup__initials { font-size: 50px; letter-spacing: 1px; }
  .lockup__tail { font-size: 22px; letter-spacing: 1px; margin-top: 4px; }
</style>
</head>
<body>

<section class="card card--front" aria-label="Business card front">
  <svg class="card__shape" width="733" height="429" viewBox="0 0 733 429" aria-hidden="true">
    <path d="M268 0 C 360 110, 360 320, 268 429 L 733 429 L 733 335 C 690 290, 680 150, 733 95 L 733 0 Z" fill="var(--white)"/>
    <path d="M268 0 C 360 110, 360 320, 268 429" fill="none" stroke="var(--red)" stroke-width="4"/>
  </svg>

  <div class="brand-mark">
    <div class="brand-mark__dot"></div>
    <div class="brand-mark__name">R.Q.T.</div>
  </div>

  <h1 class="company">Riverview <span class="company__accent">Quality</span>, &amp;<br>Training Logistics of<br>Ontario,LLC</h1>

  <div class="person">
    <div class="person__name">Owen Tash</div>
    <div class="person__title">Event and Training Specialist</div>
  </div>

  <ul class="contact-list">
    <li class="contact-list__item">
      <svg class="contact-list__icon" viewBox="0 0 24 24" aria-hidden="true"><circle cx="12" cy="12" r="12" fill="var(--red)"/><rect x="8.5" y="5.5" width="7" height="13" rx="1.3" fill="none" stroke="#fff" stroke-width="1.5"/><circle cx="12" cy="16" r="0.9" fill="#fff"/></svg>
      555.010.2002
    </li>
    <li class="contact-list__item">
      <svg class="contact-list__icon" viewBox="0 0 24 24" aria-hidden="true"><circle cx="12" cy="12" r="12" fill="var(--red)"/><path d="M6 10 Q12 5 18 10 L16.5 11.5 L14.5 10 L9.5 10 L7.5 11.5 Z" fill="#fff"/><rect x="8" y="12" width="8" height="5" rx="1" fill="#fff"/></svg>
      555.014.7890
    </li>
    <li class="contact-list__item">
      <svg class="contact-list__icon" viewBox="0 0 24 24" aria-hidden="true"><circle cx="12" cy="12" r="12" fill="var(--red)"/><g fill="none" stroke="#fff" stroke-width="1.2"><circle cx="12" cy="12" r="6.5"/><ellipse cx="12" cy="12" rx="3" ry="6.5"/><line x1="5.5" y1="12" x2="18.5" y2="12"/></g></svg>
      www.rvqtlo.com
    </li>
    <li class="contact-list__item">
      <svg class="contact-list__icon" viewBox="0 0 24 24" aria-hidden="true"><circle cx="12" cy="12" r="12" fill="var(--red)"/><rect x="6" y="8" width="12" height="8.5" fill="#fff"/><path d="M6 8 L12 13 L18 8" fill="none" stroke="var(--red)" stroke-width="1.2"/></svg>
      o.tash@rvqtlo.com
    </li>
  </ul>
</section>

<section class="card card--back" aria-label="Business card back">
  <div class="lockup">
    <div class="lockup__dot"></div>
    <div class="lockup__name">
      <div class="lockup__initials">R.Q.T.</div>
      <div class="lockup__tail">SOLUTIONS OF ON</div>
    </div>
  </div>
</section>

</body>
</html>
```